Poster for homelessness project (2 day deadline)

Amber Lantern Scheme is an initiative in the UK which aims to ensure that people who are new to sleeping on the street are quickly given assistance to take them out of situation they find themselves in.

It began as a London-based project but is now being rolled out nationwide. I am working for a project based in the north of England.

We need some posters which show an image of a place where a rough sleeper may spend the night with some supporting graphic design.

I have three initial images, but I need to be able to easily swap out the images for others. I would appreciate if you could produce three posters for me, each with a different image.

-
Please note:
My client is quite vague about what they want at the moment and the above words may change. I need the selected product to be a layered raw file that I can amend myself with any Adobe CS5.5 (or below) application.

Any typefaces that you choose need to be easily purchasable online.

Please view formatinfo.pdf for formatting guidelines.

Target Market(s)

The general public. It will be placed in public places.

Industry/Entity Type

Graphic Design

Requirements
Must have
• Must contain the words:

"Tonight someone will sleep rough for the first time. Help us make sure they find the Amber Lantern."

"Would you sleep here? Sleeping rough is dangerous. Make sure everyone finds the Amber Lantern."

-
Nice to have
• I'd like this to be quite bleak, grimy and "urban" in feel.

You may recolour/tint the images in any way to enhance this feeling.

```html
<!DOCTYPE html>
<html lang="en">
<head>
<meta charset="utf-8">
<title>Amber Lantern Scheme – Tonight Someone Will Sleep Rough</title>
<link rel="stylesheet" href="https://fonts.googleapis.com/css2?family=Inter:ital,wght@0,400;0,700;0,800;1,400;1,700&display=swap">
<style>
  :root {
    --alert-red: #ff0a1e;
    --fog-pink: #d7737f;
    --dusk-rose: #b2424f;
    --deep-maroon: #6e1420;
    --ghost-white: rgba(255, 255, 255, 0.62);
    --halo-white: rgba(255, 255, 255, 0.12);
    --pure-white: #ffffff;
  }
  * { box-sizing: border-box; margin: 0; padding: 0; }
  html, body { width: 1200px; height: 848px; overflow: hidden; background: var(--deep-maroon); }
  .poster {
    position: relative;
    width: 1200px;
    height: 848px;
    overflow: hidden;
    font-family: "Inter", "Helvetica Neue", Arial, sans-serif;
    color: var(--pure-white);
  }
  .scene-photo {
    position: absolute;
    inset: 0;
    background:
      radial-gradient(ellipse 50% 45% at 68% 58%, #e49aa3 0%, var(--fog-pink) 45%, transparent 80%),
      radial-gradient(ellipse 35% 45% at 92% 8%, var(--deep-maroon) 0%, transparent 70%),
      radial-gradient(ellipse 40% 40% at 10% 95%, #7a1d29 0%, transparent 75%),
      linear-gradient(180deg, var(--dusk-rose) 0%, #c25a67 45%, #8f2a36 100%);
  }
  .halo-rings { position: absolute; inset: 0; }
  .headline { position: absolute; left: 0; top: 0; font-size: 16px; }
  .headline-line {
    position: absolute; left: 0; display: block; white-space: nowrap;
    line-height: 1; font-weight: 800; letter-spacing: -0.05em;
  }
  .line-tonight { top: -18px; font-size: 160px; color: var(--ghost-white); }
  .line-someone { top: 125px; font-size: 124px; color: var(--ghost-white); letter-spacing: -0.04em; }
  .line-sleep   { top: 218px; font-size: 130px; color: var(--ghost-white); letter-spacing: -0.06em; }
  .line-rough   { top: 323px; font-size: 126px; color: var(--alert-red); }
  .line-first   { top: 431px; font-size: 98px; letter-spacing: -0.06em; }
  .line-time    { top: 530px; font-size: 130px; letter-spacing: -0.03em; }
  .outline-word { color: transparent; -webkit-text-stroke: 1.6px var(--ghost-white); }
  .solid-word { color: var(--ghost-white); }
  .tagline {
    position: absolute; left: 7px; top: 643px;
    font-size: 19px; font-style: italic; font-weight: 400; color: var(--pure-white);
  }
  .tagline strong { font-weight: 700; }
  .support-copy { position: absolute; left: 6px; top: 676px; width: 236px; }
  .support-copy p { font-size: 8px; line-height: 1.3; margin-bottom: 6px; color: var(--pure-white); }
  .hotline {
    position: absolute; left: 240px; top: 702px;
    display: flex; align-items: center; gap: 10px;
    font-size: 90px; font-weight: 700; letter-spacing: -0.03em; line-height: 1;
    color: var(--alert-red); white-space: nowrap;
  }
  .hotline svg { width: 62px; height: 62px; flex: none; }
  .scheme-mark {
    position: absolute; left: 4px; top: 790px;
    display: flex; align-items: center; gap: 5px;
  }
  .scheme-mark .mark-square { width: 14px; height: 14px; background: var(--alert-red); flex: none; }
  .scheme-mark .mark-name { font-size: 9.5px; font-weight: 800; color: var(--pure-white); width: 52px; line-height: 1.1; }
  .footer-copy { position: absolute; left: 68px; top: 806px; width: 520px; }
  .footer-copy p { font-size: 6.2px; line-height: 1.35; font-weight: 700; color: var(--pure-white); }
</style>
</head>
<body>
<main class="poster">
  <div class="scene-photo" role="img" aria-label="Red-tinted photograph of an empty park bench beside a path on a foggy autumn morning, trees fading into the mist"></div>

  <svg class="halo-rings" width="1200" height="848" viewBox="0 0 1200 848" aria-hidden="true">
    <circle cx="760" cy="700" r="700" fill="var(--halo-white)"/>
    <circle cx="820" cy="530" r="350" fill="var(--halo-white)"/>
    <circle cx="860" cy="592" r="286" fill="var(--halo-white)"/>
  </svg>

  <h1 class="headline">
    <span class="headline-line line-tonight">Tonight</span>
    <span class="headline-line line-someone">Someone</span>
    <span class="headline-line line-sleep">WillSleep</span>
    <span class="headline-line line-rough">Rough</span>
    <span class="headline-line line-first"><span class="outline-word">ForThe</span><span class="solid-word">First</span></span>
    <span class="headline-line line-time outline-word">Time...</span>
  </h1>

  <p class="tagline">Help us make sure they <strong>find</strong> the Amber Lantern.</p>

  <div class="support-copy">
    <p>Every night new faces arrive on our streets. A quick response can change the whole story for them.</p>
    <p>Outreach teams work through the night to find people sleeping out and offer a safe place fast.</p>
    <p>If you see someone sleeping rough, call us and tell us where. We will do the rest.</p>
  </div>

  <div class="hotline">
    <svg viewBox="0 0 24 24" aria-hidden="true"><path fill="var(--alert-red)" d="M6.6 10.8a15.1 15.1 0 0 0 6.6 6.6l2.2-2.2a1 1 0 0 1 1-.25 11.4 11.4 0 0 0 3.6.57 1 1 0 0 1 1 1V20a1 1 0 0 1-1 1A17 17 0 0 1 3 4a1 1 0 0 1 1-1h3.5a1 1 0 0 1 1 1c0 1.25.2 2.45.57 3.57a1 1 0 0 1-.25 1z"/></svg>
    <span>Call - 0800 555 0142</span>
  </div>

  <div class="scheme-mark">
    <span class="mark-square"></span>
    <span class="mark-name">Amber Lantern Scheme</span>
  </div>

  <div class="footer-copy">
    <p>The Amber Lantern Scheme connects people new to the streets with shelter, advice and support within hours of being found. Calls are answered day and night.</p>
    <p>Your call could be the first step towards a warm bed and a safe way off the streets.</p>
  </div>
</main>
</body>
</html>
```